Postcard bar mitzvah invitations

I'm looking for glossy postcards which which contain information for my son's bar mitzvah - the time and place of the service, that it will be followed by a luncheon, the time and place of the party, and how to RSVP.

```html
<!DOCTYPE html>
<html lang="en">
<head>
<meta charset="utf-8">
<title>Ethan Michael Lovett – Bar Mitzvah Invitation</title>
<link rel="stylesheet" href="https://fonts.googleapis.com/css2?family=Arimo:wght@400;700&family=Cormorant+SC:wght@500;600&display=swap">
<style>
  :root {
    --backdrop: #ece8e2;
    --card: #ffffff;
    --ink-grey: #3d4347;
    --ink-black: #121212;
    --teal: #2a9ac0;
    --teal-text: #2e9dc4;
    --star-deep: #2b3fa8;
    --star-light: #2fc6f0;
  }
  * { margin: 0; padding: 0; box-sizing: border-box; }
  html, body { width: 1200px; height: 1015px; overflow: hidden; }
  body { background: var(--backdrop); position: relative; }

  .invitation {
    position: absolute; left: 84px; top: 111px;
    width: 1032px; height: 792px;
    background: var(--card); overflow: hidden;
    box-shadow: 0 2px 10px rgba(0,0,0,0.12);
  }
  .invitation__swoosh { position: absolute; inset: 0; }

  .honoree {
    position: absolute; left: 80px; top: 40px;
    font-family: "Arimo", Arial, sans-serif; font-weight: 700;
    font-size: 72px; line-height: 75px; letter-spacing: -1px;
  }
  .honoree span { display: block; }
  .honoree__first { color: var(--ink-grey); }
  .honoree__middle { color: var(--ink-black); }
  .honoree__last { color: var(--teal); }

  .star { position: absolute; left: 166px; top: 318px; width: 145px; height: 165px; }

  .details {
    position: absolute; right: 78px; top: 108px; width: 540px;
    text-align: right; color: var(--teal-text);
    font-family: "Cormorant SC", Georgia, serif; font-weight: 500;
  }
  .details p { font-size: 25px; line-height: 31px; }
  .details .block { margin-bottom: 13px; }
  .details .name { font-size: 44px; line-height: 50px; margin: 2px 0 10px; }
  .details .hosts { font-size: 31px; line-height: 38px; margin-top: 18px; }

  .rsvp {
    position: absolute; left: 53px; top: 674px; width: 400px;
    text-align: center; color: var(--teal);
    font-family: "Arimo", Arial, sans-serif; font-size: 22px; line-height: 28px;
  }
  .rsvp svg { width: 22px; height: 22px; vertical-align: -4px; }
</style>
</head>
<body>
  <main class="invitation">
    <svg class="invitation__swoosh" viewBox="0 0 1032 792" aria-hidden="true">
      <defs>
        <linearGradient id="wash" x1="0" y1="0" x2="1" y2="1">
          <stop offset="0" stop-color="#ffffff"/>
          <stop offset="0.55" stop-color="#eef0f4"/>
          <stop offset="1" stop-color="#e2e5ec"/>
        </linearGradient>
      </defs>
      <path d="M540 0 H1032 V792 H0 V270 C200 330 330 420 430 560 C500 660 700 740 1032 700 V600 C820 560 700 420 620 260 C580 170 560 80 540 0 Z" fill="url(#wash)"/>
      <path d="M0 210 C220 250 380 380 470 520 C560 660 720 760 900 792 H0 Z" fill="#f1f2f6" opacity="0.8"/>
      <path d="M0 260 C200 290 360 400 450 560 C520 690 600 760 680 792 H420 C360 700 260 520 0 430 Z" fill="#ffffff" opacity="0.85"/>
      <path d="M560 0 C600 200 720 420 1032 600" fill="none" stroke="#ffffff" stroke-width="6" opacity="0.9"/>
      <path d="M0 245 C240 280 410 420 500 600" fill="none" stroke="#dfe2ea" stroke-width="2"/>
    </svg>

    <h1 class="honoree">
      <span class="honoree__first">ETHAN</span>
      <span class="honoree__middle">MICHAEL</span>
      <span class="honoree__last">LOVETT</span>
    </h1>

    <svg class="star" viewBox="0 0 145 165" aria-hidden="true">
      <defs>
        <radialGradient id="starFill" cx="0.5" cy="0.5" r="0.55">
          <stop offset="0.35" stop-color="#2fc6f0"/>
          <stop offset="1" stop-color="#2b3fa8"/>
        </radialGradient>
      </defs>
      <g fill="none" stroke="url(#starFill)" stroke-width="14" stroke-linejoin="miter">
        <polygon points="72.5,10 136,120 9,120"/>
        <polygon points="72.5,155 136,45 9,45"/>
      </g>
    </svg>

    <section class="details">
      <div class="block">
        <p>With Great Pride and honor</p>
        <p>We invite you to share our</p>
        <p>happiness as our son</p>
      </div>
      <p class="name">ETHAN MICHAEL</p>
      <div class="block">
        <p>Is Called To the Torah</p>
        <p>To Become a Bar Mitzvah</p>
      </div>
      <div class="block">
        <p>Saturday, June 13, 2015</p>
        <p>at ten thirty in the morning</p>
      </div>
      <div class="block">
        <p>Temple Beth Shalom</p>
        <p>1280 Maple Grove Road,</p>
        <p>Cedar Falls, Ohio 44100</p>
      </div>
      <div class="block">
        <p>Luncheon to follow the service</p>
      </div>
      <div class="block">
        <p>Party at seven in the evening</p>
        <p>The Lakeview Room, 200 Shore Drive,</p>
        <p>Cedar Falls, Ohio 44100</p>
      </div>
      <p class="hosts">Karen &amp; Paul Lovett</p>
    </section>

    <footer class="rsvp">
      <p>Please RSVP by May 31, 2015</p>
      <p>Karen at karenlov@mailbox.net</p>
      <p>or <svg viewBox="0 0 24 24" role="img" aria-label="phone"><circle cx="12" cy="12" r="10.5" fill="none" stroke="currentColor" stroke-width="1.6"/><path d="M9 6.5 c-1.6 1 -1.8 3.5 -0.5 6 s3.6 4.6 5.5 4.8 l1.2 -1.7 -2.2 -1.6 -1 .8 c-.9 -.5 -2 -1.9 -2.3 -3 l1 -.6 -.9 -2.6 z" fill="currentColor"/></svg>555.014.2368</p>
    </footer>
  </main>
</body>
</html>
```